Software Company Requires Website

We need a web design for a new mobile software development company based in London named Velquin Solutions.
The design needs to be clean and smooth. Not too flashy, not too boring.
I would like to try the design with some warm colors, and maybe a headline or something highlighted with a strong color. ( logo ? ) The layout should be something like the bellow links, all in one page.

http://brantelo.net/
http://www.kelvory.com/
http://www.work-plover.de/
http://www.tusker.com/
http://www.quildenta.com/us/

Now some of them they seem different from the others, but in each of them there is something that ticks my brain, so it`s up to you to surprise me.

I have uploaded the logo of the company, so you guys can fit that in your design as well.
Updates

Hy everybody This will be the last update for the brief. The company will focus in the beginning for mobile development only, so i would like the website design to be done in a matter that will reflect that. We will develop IOS, Android and Windows applications. We will also require 3 pages: One for the home menu, one for portfolio and one for contact us. The layout should be the same ( one page scroll down ) but the design of the 3 pages different. Please readdress the brief. Hope that i provided enough information for the scope of the project.

I have uploaded the logo that you guys can use. If the logo requires small modifications you can adjust that to suit your idea as long as the logo does not change completely.

Target Market(s)

High End companies that require simplified software solutions.

Industry/Entity Type

It Company

Number of Pages Required

3 page

Requirements
Must have
• One page scroll down layout for 3 pages:
• one for home page, one for portfolio and one for contact us.
• In the portfolio page we would like to have different display options for given examples of applications ( min 3 )

```html
<!DOCTYPE html>
<html lang="en">
<head>
<meta charset="utf-8">
<title>Velquin Solutions</title>
<link href="https://fonts.googleapis.com/css2?family=Raleway:wght@400;500;600;700&family=Open+Sans:wght@400;600;700&display=swap" rel="stylesheet">
<style>
:root{
  --blue:#1e73c2;
  --blue-dark:#1a64aa;
  --white:#ffffff;
  --ink:#333333;
  --muted:#666666;
  --hero-a:#3a3632;
  --hero-b:#1c1b1a;
  --footer:#353b44;
  --footer-bar:#2b3038;
  --footer-line:#4d545e;
}
*{margin:0;padding:0;box-sizing:border-box}
html,body{width:1200px;height:4027px;overflow:hidden}
body{position:relative;font-family:'Open Sans',Arial,sans-serif;background:var(--white);color:var(--ink)}
.abs{position:absolute}

/* header */
.site-header{left:0;top:0;width:1200px;height:81px;background:var(--white)}
.brand{left:110px;top:22px;display:flex;align-items:center;gap:10px;font-family:'Raleway',Arial,sans-serif;font-weight:600;font-size:24px;color:var(--blue)}
.brand-dot{width:26px;height:26px;border-radius:50%;border:3px solid var(--blue)}
.main-nav a{position:absolute;top:33px;font-family:'Raleway',Arial,sans-serif;font-size:15px;font-weight:500;color:#777;text-decoration:none;letter-spacing:.3px}
.main-nav a.active{color:var(--blue);font-weight:700}
.nav-underline{left:583px;top:76px;width:56px;height:5px;background:var(--blue)}

/* hero */
.hero{left:0;top:81px;width:1200px;height:681px;background:radial-gradient(ellipse at 35% 55%,var(--hero-a),var(--hero-b) 75%)}
.hero-mark{left:582px;top:232px;width:36px;height:36px;border-radius:50%;border:3px solid var(--white)}
.hero-title{left:0;top:306px;width:1200px;text-align:center;font-family:'Raleway',Arial,sans-serif;font-weight:700;font-size:44px;color:var(--white)}
.hero-sub{left:0;top:364px;width:1200px;text-align:center;font-family:'Raleway',Arial,sans-serif;font-weight:600;font-size:17px;letter-spacing:2px;color:var(--white)}
.store-btn{top:426px;height:36px;border:2px solid var(--white);border-radius:3px;color:var(--white);font-size:14px;display:flex;align-items:center;gap:8px;padding:0 12px}
.store-btn i{width:12px;height:16px;border:2px solid var(--white);border-radius:2px;display:block}
.start{left:552px;top:570px;width:96px;height:96px;border-radius:50%;background:#1c1c1c;border:3px solid var(--white);color:var(--white);text-align:center;font-family:'Raleway',Arial,sans-serif;font-weight:700;font-size:20px;padding-top:22px}

/* blue */
.blue-band{left:0;top:762px;width:1200px;height:2084px;background:var(--blue)}
.spine{left:599px;width:3px;background:var(--white)}
.node{width:20px;height:20px;border-radius:50%;background:var(--white);border:4px solid #222;margin-left:-10px}
.section-tag{left:454px;width:292px;height:56px;background:var(--white);color:var(--blue);text-align:center;line-height:56px;font-family:'Raleway',Arial,sans-serif;font-size:30px;font-weight:500}
.hub{width:92px;height:92px;border-radius:50%;background:var(--white);border:5px solid var(--blue);box-shadow:0 0 0 4px var(--white);margin-left:-46px;display:flex;align-items:center;justify-content:center}

.svc-line{left:215px;top:1041px;width:773px;height:3px;background:var(--white)}
.svc{width:240px;text-align:center;color:var(--white)}
.svc-icon{width:62px;height:62px;border-radius:50%;border:3px solid var(--white);background:var(--blue);margin:0 auto;display:flex;align-items:center;justify-content:center}
.svc h3{font-family:'Open Sans',Arial,sans-serif;font-size:16px;font-weight:700;margin-top:22px}
.svc p{font-size:13px;line-height:20px;margin-top:14px}
.svc a{display:block;font-size:12px;font-style:italic;color:var(--white);text-decoration:none;margin-top:16px}

.testimonial{left:225px;top:1624px;width:747px;height:422px;background:var(--white)}
.testimonial-photo{left:0;top:0;width:374px;height:422px;background:linear-gradient(135deg,#6f5a45,#2e3338 60%,#8a7b6a)}
.testimonial-name{left:409px;top:46px;font-family:'Raleway',Arial,sans-serif;font-size:30px;color:#222}
.testimonial-name b{font-family:'Open Sans',Arial,sans-serif;font-weight:700}
.testimonial-text{left:409px;top:108px;width:310px;font-size:15px;line-height:28px;color:var(--muted)}
.testimonial-company{left:409px;top:280px;font-size:15px;color:var(--blue)}

.tile{width:320px;height:184px}
.tile-overlay{left:161px;top:0;width:159px;height:184px;background:rgba(0,0,0,.75)}
.tile-plus{left:206px;top:30px;width:68px;height:68px;border:2px solid var(--white);border-radius:3px}
.tile-more{left:196px;top:124px;width:88px;height:32px;border:2px solid var(--white);border-radius:3px;color:var(--white);font-size:11px;font-weight:600;text-align:center;line-height:28px}

/* contact */
.contact-tag{background:var(--blue);color:var(--white)}
.contact-panel{left:110px;top:3085px;width:980px;height:553px;background:var(--blue)}
.field{height:51px;border:2px solid var(--white);border-radius:4px;color:var(--white);font-size:14px;padding:12px 10px}
.send{left:373px;top:406px;width:237px;height:56px;border:2px solid var(--white);border-radius:3px;color:var(--white);font-family:'Raleway',Arial,sans-serif;font-weight:700;font-size:14px;text-align:center;line-height:52px}

/* footer */
.site-footer{left:0;top:3740px;width:1200px;height:220px;background:var(--footer)}
.social{top:3841px;width:66px;height:66px;border-radius:50%;border:3px solid var(--footer-line)}
.footer-bar{left:0;top:3960px;width:1200px;height:67px;background:var(--footer-bar);color:#7d848e;font-size:13px}
.footer-bar span{position:absolute;top:24px}
</style>
</head>
<body>

<header class="abs site-header">
  <div class="abs brand"><span class="brand-dot"></span>Velquin Solutions</div>
  <nav class="main-nav">
    <a class="active" style="left:588px">HOME</a>
    <a style="left:671px">ABOUT US</a>
    <a style="left:781px">SERVICES</a>
    <a style="left:884px">PORTFOLIO</a>
    <a style="left:1003px">CONTACT US</a>
  </nav>
  <div class="abs nav-underline"></div>
</header>

<section class="abs hero" role="img" aria-label="Dark photograph of hands using a smartphone"></section>
<div class="abs hero-mark"></div>
<h1 class="abs hero-title">WE ARE A CREATIVE</h1>
<p class="abs hero-sub">SOFTWEAR DEVELOPER</p>
<div class="abs store-btn" style="left:470px"><i></i>App Harbor</div>
<div class="abs store-btn" style="left:610px"><i style="border-radius:0;border-width:0 0 0 0;border-left:10px solid #fff;border-top:7px solid transparent;border-bottom:7px solid transparent;width:0;height:0"></i>Play Vault</div>
<div class="abs spine" style="top:666px;height:96px"></div>
<div class="abs start">Start
  <svg width="20" height="14" viewBox="0 0 20 14" style="display:block;margin:4px auto 0"><path d="M4 4l6 6 6-6" stroke="#fff" stroke-width="3" fill="none"/></svg>
</div>

<section class="abs blue-band"></section>
<div class="abs spine" style="top:762px;height:2084px"></div>
<div class="abs node" style="left:600px;top:752px"></div>

<!-- services -->
<h2 class="abs section-tag" style="top:886px">OUR SERVICES</h2>
<div class="abs svc-line"></div>
<div class="abs spine" style="left:214px;top:1041px;height:23px"></div>
<div class="abs spine" style="left:471px;top:1041px;height:23px"></div>
<div class="abs spine" style="left:729px;top:1041px;height:23px"></div>
<div class="abs spine" style="left:987px;top:1041px;height:23px"></div>
<div class="abs hub" style="left:600px;top:996px"><span style="width:34px;height:34px;border-radius:50%;background:var(--blue)"></span></div>

<div class="abs svc" style="left:95px;top:1064px">
  <div class="svc-icon"><svg width="22" height="30" viewBox="0 0 22 30"><rect x="2" y="2" width="18" height="26" rx="3" fill="none" stroke="#fff" stroke-width="2.5"/><circle cx="11" cy="23" r="1.8" fill="#fff"/></svg></div>
  <h3>MOBILE</h3>
  <p>Lorem ipsum dolor sit consectetur adipiscing elit sed eiusmod tempor incididunt ut labore et dolore.</p>
  <a>Read more..</a>
</div>
<div class="abs svc" style="left:352px;top:1064px">
  <div class="svc-icon"><svg width="32" height="28" viewBox="0 0 32 28"><path d="M3 3h18v12H10l-5 4v-4H3z" fill="none" stroke="#fff" stroke-width="2.5" stroke-linejoin="round"/><path d="M14 18h10l4 4v-4h1V9h-5" fill="none" stroke="#fff" stroke-width="2.5" stroke-linejoin="round"/></svg></div>
  <h3>SOCIAL</h3>
  <p>Lorem ipsum dolor sit consectetur adipiscing elit sed eiusmod tempor incididunt ut labore et dolore.</p>
  <a>Read more..</a>
</div>
<div class="abs svc" style="left:610px;top:1064px">
  <div class="svc-icon"><svg width="32" height="28" viewBox="0 0 32 28"><rect x="2" y="3" width="28" height="18" rx="2" fill="none" stroke="#fff" stroke-width="2.5"/><path d="M11 26h10M16 21v5" stroke="#fff" stroke-width="2.5"/></svg></div>
  <h3>DIGITAL</h3>
  <p>Lorem ipsum dolor sit consectetur adipiscing elit sed eiusmod tempor incididunt ut labore et dolore.</p>
  <a>Read more..</a>
</div>
<div class="abs svc" style="left:868px;top:1064px">
  <div class="svc-icon"><svg width="32" height="32" viewBox="0 0 32 32"><circle cx="13" cy="13" r="8" fill="none" stroke="#fff" stroke-width="2.5" stroke-dasharray="4 2"/><circle cx="13" cy="13" r="3" fill="#fff"/><circle cx="23" cy="23" r="5" fill="none" stroke="#fff" stroke-width="2.5" stroke-dasharray="3 2"/></svg></div>
  <h3>EXPERIENTIAL</h3>
  <p>Lorem ipsum dolor sit consectetur adipiscing elit sed eiusmod tempor incididunt ut labore et dolore.</p>
  <a>Read more..</a>
</div>
<div class="abs node" style="left:600px;top:1346px"></div>

<!-- testimonials -->
<h2 class="abs section-tag" style="top:1469px">TESTIMONIALS</h2>
<div class="abs testimonial">
  <div class="abs testimonial-photo" role="img" aria-label="Photograph of a young couple looking at a camera"></div>
  <div class="abs testimonial-name">MARCUS <b>DELANEY</b></div>
  <p class="abs testimonial-text">Lorem ipsum dolor consectetur adipiscing sed do eiusmod tempor incididunt labore et dolore magna aliqua. Ut enim ad minim veniam, quis nostrud exercitation ullamco laboris nisi ut aliquip ex ea commodo.</p>
  <div class="abs testimonial-company">Orvane Company</div>
</div>
<div class="abs hub" style="left:600px;top:1578px"><svg width="44" height="34" viewBox="0 0 44 34"><path d="M2 18c0-9 5-15 13-16v6c-4 1-6 4-6 7h6v15H2zM25 18c0-9 5-15 13-16v6c-4 1-6 4-6 7h6v15H25z" fill="#1e73c2"/></svg></div>
<div class="abs node" style="left:600px;top:2036px"></div>

<!-- portfolio -->
<h2 class="abs section-tag" style="top:2199px">OUR PORTFOLIO</h2>
<div class="abs tile" style="left:110px;top:2374px;background:linear-gradient(135deg,#2f4a36,#0f1a14 60%,#45604a)" role="img" aria-label="App screenshot on a phone with green theme">
  <div class="abs tile-overlay"></div>
  <div class="abs tile-plus"><svg width="64" height="64" viewBox="0 0 64 64"><path d="M32 14v36M14 32h36" stroke="#fff" stroke-width="3"/></svg></div>
  <div class="abs tile-more">READ MORE</div>
</div>
<div class="abs tile" style="left:440px;top:2374px;background:radial-gradient(circle at 60% 40%,#1d4a1d,#050805 70%)" role="img" aria-label="Dark app interface screens with green network graphic"></div>
<div class="abs tile" style="left:771px;top:2374px;background:linear-gradient(135deg,#3b3f48,#8a6a3a 50%,#c9ccd2)" role="img" aria-label="Tablet with colourful app icons"></div>
<div class="abs tile" style="left:110px;top:2570px;background:linear-gradient(135deg,#3a2030,#8a3a5a 55%,#2a2a2e)" role="img" aria-label="Tablet and phones showing a cosmetics app"></div>
<div class="abs tile" style="left:440px;top:2570px;background:linear-gradient(135deg,#6a2e14,#c2622a 50%,#2e4a1a)" role="img" aria-label="Phones showing a pizza ordering app"></div>
<div class="abs tile" style="left:771px;top:2570px;background:linear-gradient(135deg,#0d2a4a,#1f6aa8 55%,#0a1a30)" role="img" aria-label="Blue digital app icons floating above a hand"></div>
<div class="abs hub" style="left:600px;top:2309px"><svg width="40" height="34" viewBox="0 0 40 34"><rect x="6" y="2" width="32" height="26" rx="2" fill="none" stroke="#1e73c2" stroke-width="3"/><rect x="2" y="6" width="32" height="26" rx="2" fill="#fff" stroke="#1e73c2" stroke-width="3"/><path d="M6 28l9-10 6 6 4-4 7 8z" fill="#1e73c2"/></svg></div>
<div class="abs node" style="left:600px;top:2836px"></div>

<!-- contact -->
<div class="abs spine" style="top:2846px;height:239px;background:var(--blue)"></div>
<h2 class="abs section-tag contact-tag" style="top:2927px">CONTACT US</h2>
<div class="abs contact-panel">
  <div class="abs field" style="left:40px;top:110px;width:290px">Name</div>
  <div class="abs field" style="left:345px;top:110px;width:290px">Email</div>
  <div class="abs field" style="left:650px;top:110px;width:290px">Address</div>
  <div class="abs field" style="left:40px;top:183px;width:900px;height:188px">Message</div>
  <div class="abs send">SEAND MESSAGE</div>
</div>
<div class="abs spine" style="top:3638px;height:102px;background:var(--blue)"></div>
<div class="abs hub" style="left:600px;top:3042px;background:var(--blue);border-color:var(--white);box-shadow:0 0 0 4px var(--blue)"><svg width="44" height="32" viewBox="0 0 44 32"><rect x="2" y="2" width="40" height="28" fill="none" stroke="#fff" stroke-width="3"/><path d="M2 2l20 16L42 2" fill="none" stroke="#fff" stroke-width="3"/></svg></div>
<div class="abs node" style="left:600px;top:3628px;border-color:var(--blue)"></div>

<!-- footer -->
<footer class="abs site-footer"></footer>
<div class="abs hub" style="left:600px;top:3767px;background:var(--blue);border-color:var(--white);box-shadow:none"><svg width="32" height="20" viewBox="0 0 32 20"><path d="M4 16L16 4l12 12" stroke="#fff" stroke-width="5" fill="none"/></svg></div>
<div class="abs social" style="left:329px" aria-label="Social profile"></div>
<div class="abs social" style="left:427px" aria-label="Social profile"></div>
<div class="abs social" style="left:525px" aria-label="Social profile"></div>
<div class="abs social" style="left:623px" aria-label="Social profile"></div>
<div class="abs social" style="left:721px" aria-label="Social profile"></div>
<div class="abs social" style="left:819px" aria-label="Social profile"></div>
<div class="abs footer-bar">
  <span style="left:110px">Copy right © 2014 Velquin solutions . All rights reserved.</span>
  <span style="left:1002px">Privacy Policy</span>
</div>

</body>
</html>
```